Mental Health Counselor needs advertisement design for Men's and Woman's chorus programs

I need a 1/6th page advertisement for my mental health practice named 'Quarry Bay Mental Health' I primarily serve the LGBTQ community, providing individual and couples/family therapy. The ad should include a 'call to action' such as Call me I can help, or Schedule an appointment today. The final design should convey familiarity with the needs of the queer community and my unique ability to help the reader with emotional concerns or relationship issues.

I would like to see designs using my logo (attached 2015-Logo.eps) and the colors of my website http://www.quarrybaymentalhealth.example particularly the banner imagery (attached quarrybay banner.jpg and quarrybayMH2015.ase, bannersource.jpg)

The ad must contain the following:
Quarry Bay Mental Health or Quarry Bay Mental Health Counseling
the website address www.quarrybaymentalhealth.example
phone number 206-555-0148
and my name/title: Dorian K. Whitlock Jr. MA, LMHCA/LMFTA

I am attaching the guidelines for the ad and a pdf sample of their program,

Target Market(s)

Gay, Bisexual and Transgender clients with reasonable affluence, in their late 30's- late 50's

Industry/Entity Type

Mental Health

Font styles to use
Sans Serif
Other font styles liked:
• Clerica Medium, Open Sans Family

Colors
b7a5cd
d7cce4
0455a3
ffffff

Requirements
Must have
• Must use my Logo (2015-Logo.eps attached)
Should not have
• Biased or negative language.

```html
<!DOCTYPE html>
<html lang="en">
<head>
<meta charset="utf-8">
<title>Quarry Bay Mental Health Counseling – Ad Options</title>
<link rel="stylesheet" href="https://fonts.googleapis.com/css2?family=Oswald:wght@500;600&family=Open+Sans:wght@400;700&display=swap">
<style>
  :root {
    --navy-deep: #12124f;
    --navy-mid: #2a3a78;
    --navy-glow: #4a6496;
    --lavender: #b7a5cd;
    --lavender-light: #d7cce4;
    --logo-blue: #0455a3;
    --strip-blue: #00a3dc;
    --gold: #f7c928;
    --white: #ffffff;
    --page: #ffffff;
  }
  html, body {
    margin: 0;
    padding: 0;
    width: 1200px;
    height: 1200px;
    overflow: hidden;
    background: var(--page);
  }
  .canvas {
    position: relative;
    width: 1200px;
    height: 1200px;
  }
  .ad {
    position: absolute;
    overflow: hidden;
    background: linear-gradient(90deg, var(--navy-deep) 0%, var(--navy-mid) 35%, var(--navy-glow) 60%, var(--navy-mid) 82%, var(--navy-deep) 100%);
    color: var(--white);
  }
  .ad--wide-art { left: 79px; top: 70px; width: 1042px; height: 520px; }
  .ad--centered { left: 76px; top: 617px; width: 1051px; height: 523px; }

  .skyline {
    position: absolute;
    left: 0;
    right: 0;
    background: linear-gradient(180deg, rgba(60,80,130,0) 0%, rgba(70,90,140,0.45) 55%, rgba(40,50,100,0.6) 100%);
  }
  .ad--wide-art .skyline { top: 330px; height: 133px; }
  .ad--centered .skyline { top: 340px; height: 127px; }

  .session-art {
    position: absolute;
    border-radius: 6px;
  }
  .ad--wide-art .session-art {
    left: 490px; top: 20px; width: 530px; height: 440px;
    background: radial-gradient(ellipse at 55% 50%, rgba(200,205,225,0.18) 0%, rgba(200,205,225,0.06) 60%, rgba(200,205,225,0) 100%);
  }
  .ad--centered .session-art {
    left: 146px; top: 276px; width: 182px; height: 142px;
    background: radial-gradient(ellipse at 50% 50%, rgba(255,255,255,0.28) 0%, rgba(255,255,255,0.08) 70%, rgba(255,255,255,0) 100%);
  }

  .brand-mark {
    position: absolute;
    width: 96px;
    height: 96px;
    border-radius: 50%;
    background: var(--lavender);
  }
  .ad--wide-art .brand-mark { left: 52px; top: 52px; }
  .ad--centered .brand-mark { left: 54px; top: 48px; }

  .practice-name {
    position: absolute;
    margin: 0;
    font-family: "Oswald", "Arial Narrow", sans-serif;
    font-weight: 600;
    text-transform: uppercase;
    letter-spacing: 5px;
    line-height: 1.12;
    color: var(--white);
  }
  .ad--wide-art .practice-name { left: 187px; top: 40px; font-size: 50px; }
  .ad--centered .practice-name { left: 190px; top: 36px; width: 800px; font-size: 54px; text-align: center; }

  .call-to-action {
    position: absolute;
    margin: 0;
    font-family: "Open Sans", Arial, sans-serif;
    font-weight: 700;
    color: var(--gold);
    line-height: 1.22;
  }
  .ad--wide-art .call-to-action { left: 187px; top: 190px; font-size: 34px; }
  .ad--centered .call-to-action { left: 0; width: 1051px; top: 184px; font-size: 42px; text-align: center; }

  .counselor {
    position: absolute;
    font-family: "Open Sans", Arial, sans-serif;
    font-weight: 700;
  }
  .counselor__name { display: block; }
  .counselor__credentials { display: block; }
  .ad--wide-art .counselor { left: 187px; top: 295px; }
  .ad--wide-art .counselor__name { font-size: 27px; }
  .ad--wide-art .counselor__credentials { font-size: 18px; margin-top: 4px; }
  .ad--centered .counselor { left: 354px; top: 267px; width: 400px; text-align: center; }
  .ad--centered .counselor__name { font-size: 29px; }
  .ad--centered .counselor__credentials { font-size: 20px; margin-top: 6px; }

  .phone {
    position: absolute;
    font-family: "Oswald", "Arial Narrow", sans-serif;
    font-weight: 500;
    letter-spacing: 0.5px;
    line-height: 1;
    color: var(--white);
  }
  .ad--wide-art .phone { left: 184px; top: 364px; font-size: 72px; }
  .ad--centered .phone { left: 370px; top: 352px; font-size: 78px; }

  .contact-strip {
    position: absolute;
    left: 0;
    right: 0;
    bottom: 0;
    background: var(--strip-blue);
    font-family: "Open Sans", Arial, sans-serif;
    font-size: 20px;
    color: var(--navy-deep);
    display: flex;
    align-items: center;
    justify-content: space-between;
    box-sizing: border-box;
  }
  .ad--wide-art .contact-strip { height: 57px; padding: 0 90px 0 54px; }
  .ad--centered .contact-strip { height: 56px; padding: 0 127px 0 38px; }
</style>
</head>
<body>
<main class="canvas">

  <section class="ad ad--wide-art">
    <div class="skyline" role="img" aria-label="Faint night view of a city skyline with a tall observation tower"></div>
    <div class="session-art" role="img" aria-label="Light outline illustration of a counselor and client seated in chairs facing each other"></div>
    <div class="brand-mark" aria-hidden="true"></div>
    <h2 class="practice-name">Quarry Bay Mental<br>Health Counseling</h2>
    <p class="call-to-action">Schedule an<br>Appointment Today</p>
    <p class="counselor" style="margin:0">
      <span class="counselor__name">Dorian K. Whitlock Jr. MA</span>
      <span class="counselor__credentials">(LMHCA/LMFTA)</span>
    </p>
    <div class="phone">206-555-0148</div>
    <footer class="contact-strip">
      <span class="contact-strip__email">dorian@quarrybaymentalhealth.example</span>
      <span class="contact-strip__web">www.quarrybaymentalhealth.example</span>
    </footer>
  </section>

  <section class="ad ad--centered">
    <div class="skyline" role="img" aria-label="Faint night view of a city skyline with a tall observation tower"></div>
    <div class="session-art" role="img" aria-label="Small white outline illustration of a counselor comforting a seated client"></div>
    <div class="brand-mark" aria-hidden="true"></div>
    <h2 class="practice-name">Quarry Bay Mental Health<br>Counseling</h2>
    <p class="call-to-action">Schedule an Appointment Today</p>
    <p class="counselor" style="margin:0">
      <span class="counselor__name">Dorian K. Whitlock Jr. MA</span>
      <span class="counselor__credentials">(LMHCA/LMFTA)</span>
    </p>
    <div class="phone">206-555-0148</div>
    <footer class="contact-strip">
      <span class="contact-strip__email">dorian@quarrybaymentalhealth.example</span>
      <span class="contact-strip__web">www.quarrybaymentalhealth.example</span>
    </footer>
  </section>

</main>
</body>
</html>
```